New (old) Business Card Design Project

I would like to purchase a customized version of a design you have previously submitted - https://www.artsubmitly.example/design/7395021

I like the card above, and would like to use the same design, jus with my business name, BRADLEY ASSET MANAGEMENT. I like the colors in the card above, as well as the font. The other side will have my name, company name, address, phone, email, website, plus disclosure text I will provide.

Target Market(s)

wealthy families

Industry/Entity Type

Financial Services

Contact Information for Business Card

logo on one side, on other my name, company, address, phone, email, website, disclosure language I will provide.

Colors

Designer to choose colors to be used in the design.

Requirements
Must have
• colors: Deep blue and white
Nice to have
• Please see the items I have uploaded, below.
Should not have
• Cheap, tacky look.

```html
<!DOCTYPE html>
<html lang="en">
<head>
<meta charset="utf-8">
<title>Bradley Asset Management – Business Card</title>
<link rel="stylesheet" href="https://fonts.googleapis.com/css2?family=Open+Sans:wght@400;600&display=swap">
<style>
  :root {
    --backdrop: #c8c9cb;
    --navy: #1b2a55;
    --paper: #ffffff;
    --ink: #111111;
  }
  * { margin: 0; padding: 0; box-sizing: border-box; }
  html, body {
    width: 1200px;
    height: 1000px;
    overflow: hidden;
    background: var(--backdrop);
    font-family: "Open Sans", sans-serif;
  }
  .canvas { position: relative; width: 1200px; height: 1000px; }
  .card {
    position: absolute;
    left: 304px;
    width: 564px;
    height: 339px;
  }
  .card--contact { top: 123px; background: var(--paper); }
  .card--brand { top: 552px; background: var(--navy); }

  .identity {
    position: absolute;
    right: 280px;
    top: 246px;
    top: 123px;
    text-align: right;
  }
  .identity { top: 124px; }
  .identity__name {
    color: var(--navy);
    font-size: 20px;
    font-weight: 600;
    line-height: 28px;
  }
  .identity__company {
    color: var(--ink);
    font-size: 14px;
    line-height: 20px;
    margin-top: 2px;
  }
  .divider {
    position: absolute;
    left: 304px;
    top: 133px;
    width: 2px;
    height: 147px;
    background: var(--navy);
  }
  .contact-list {
    position: absolute;
    left: 328px;
    top: 193px;
    list-style: none;
    color: var(--ink);
    font-size: 14.5px;
    line-height: 22px;
  }
  .contact-list__web { color: var(--navy); }

  .brand-name {
    position: absolute;
    inset: 0;
    display: flex;
    align-items: center;
    justify-content: center;
    color: var(--paper);
    font-size: 24px;
    font-weight: 400;
    letter-spacing: 2px;
  }
</style>
</head>
<body>
  <main class="canvas">
    <section class="card card--contact" aria-label="Card contact side">
      <div class="identity">
        <p class="identity__name">Name: xxxxxxxxxx</p>
        <p class="identity__company">BRADLEY ASSET</p>
      </div>
      <div class="divider"></div>
      <ul class="contact-list">
        <li>000 000 000</li>
        <li>Address: xxxxxxx</li>
        <li>xxxxx@xxx.xx.com</li>
        <li class="contact-list__web">www.xxxxxxx.com</li>
      </ul>
    </section>

    <section class="card card--brand" aria-label="Card brand side">
      <p class="brand-name">BRADLEY ASSET MANAGEMENT</p>
    </section>
  </main>
</body>
</html>
```